Hi,
We are also sourcing for a logo, if you have ideas please take a look at our other project (if you look at our profile you should be able to see it).
We are looking for a website that will be used to manage mobile devices. The feature set is rather small, users can Wipe, Lock, Locate devices as well as make them Ring or Speak (by sending text to be spoken). We attached some images of what it looks like right now. We are looking for simplicity, uniformity and most importantly, the website should be thought of as primary User Interface, it should flow.
Please see attached to get an idea of what it looks like now. The current design was inspired by making a site that will work and flow well on a variety of displays (from mobile to tablet to desktop).
We want to stay away from radio buttons, check-boxes. This should be engaging and creative, opposite of Corporate. Not busy (ideally we are looking to have fewest possible choices at any given time and at the same time no feature should be more than 3 clicks away (this is a suggestion/approximation... just want to share our understanding of what 'flow' is).
Could be cartoony.
Thanks!
BrambleKeep
Reason: there are a couple of designs that are interesting, in addition to specific feedback I provided, possibly looking for more concepts.
Thank You

```html
<!DOCTYPE html>
<html lang="en">
<head>
<meta charset="utf-8">
<title>BrambleKeep – Lost UR Phone?</title>
<link href="https://fonts.googleapis.com/css2?family=Graduate&family=Dosis:wght@500&family=Alfa+Slab+One&display=swap" rel="stylesheet">
<style>
  :root {
    --stage: #e4e4e4;
    --night: #2b2530;
    --night-deep: #1d1a22;
    --night-glow: #3e3a44;
    --pink: #d4157f;
    --pink-deep: #9e0f5f;
    --mint: #5fcfae;
    --mint-deep: #3e9f85;
    --cream: #f6e3c8;
    --ink: #1f1b22;
  }
  * { box-sizing: border-box; margin: 0; padding: 0; }
  html, body { width: 1200px; height: 848px; overflow: hidden; }
  body { background: var(--stage); position: relative; }

  .page {
    position: absolute; left: 120px; top: 18px;
    width: 959px; height: 812px; overflow: hidden;
    background: radial-gradient(ellipse at 55% 55%, var(--night-glow) 0%, var(--night) 45%, var(--night-deep) 100%);
  }
  .decor { position: absolute; inset: 0; width: 100%; height: 100%; }

  .brand {
    position: absolute; left: 671px; top: 36px; width: 232px; height: 47px;
    background: var(--pink); border-radius: 4px;
    display: flex; align-items: center; justify-content: center;
    font-family: "Dosis", sans-serif; font-weight: 500; font-size: 31px;
    color: var(--cream); letter-spacing: 0.5px;
  }

  .headline { position: absolute; left: 127px; top: 100px; height: 110px; }
  .headline span {
    position: absolute; background: var(--pink);
    font-family: "Alfa Slab One", serif; color: var(--cream);
    text-shadow: 3px 3px 0 var(--ink); line-height: 1; padding: 8px 10px;
    font-size: 62px;
  }
  .headline .word-lost  { left: 0;   top: 18px; transform: rotate(-3deg); }
  .headline .word-ur    { left: 204px; top: 0; transform: rotate(-5deg); background: var(--cream); color: var(--ink); text-shadow: none; }
  .headline .word-phone { left: 315px; top: 22px; transform: rotate(-2deg); }

  .nav { position: absolute; left: 36px; top: 328px; width: 232px; }
  .nav-item { position: relative; display: block; width: 232px; height: 80px; margin-bottom: 20px; text-decoration: none; }
  .nav-item svg { position: absolute; inset: 0; }
  .nav-item span {
    position: absolute; left: 0; right: 12px; top: 22px; text-align: center;
    font-family: "Graduate", serif; font-size: 21px; color: var(--pink);
  }

  .device {
    position: absolute; border-radius: 18px;
  }
  .device-lock { left: 360px; top: 245px; width: 200px; height: 230px; background: var(--mint); transform: rotate(14deg); }
  .device-apps { left: 375px; top: 450px; width: 250px; height: 160px; background: var(--pink); transform: rotate(-10deg); }

  .actions {
    position: absolute; left: 596px; top: 285px;
    font-family: "Graduate", serif; font-size: 62px; line-height: 64px;
    color: var(--cream); text-shadow: 4px 4px 0 var(--pink-deep);
    transform: rotate(-3deg);
  }
  .find {
    position: absolute; left: 507px; top: 600px;
    font-family: "Graduate", serif; font-size: 58px; line-height: 64px;
    color: var(--cream); text-shadow: 4px 4px 0 var(--pink-deep);
  }
  .cta {
    position: absolute; left: 513px; top: 667px; width: 281px; height: 95px;
    background: var(--pink); transform: rotate(-1.5deg);
    display: flex; align-items: center; justify-content: center;
    font-family: "Dosis", sans-serif; font-weight: 500; font-size: 44px;
    color: var(--cream); text-decoration: none;
  }
</style>
</head>
<body>
  <main class="page">
    <svg class="decor" viewBox="0 0 959 812" aria-hidden="true">
      <circle cx="1080" cy="0" r="380" fill="none" stroke="var(--cream)" stroke-width="3"/>
      <circle cx="660" cy="330" r="110" fill="none" stroke="var(--cream)" stroke-width="1.5" opacity="0.6"/>
      <path d="M0 190 Q 300 120 560 230" fill="none" stroke="var(--cream)" stroke-width="1" opacity="0.35"/>
      <circle cx="240" cy="640" r="30" fill="var(--mint-deep)" opacity="0.5"/>
      <circle cx="300" cy="520" r="70" fill="var(--mint-deep)" opacity="0.35"/>
      <circle cx="880" cy="780" r="10" fill="var(--mint)" opacity="0.8"/>
      <!-- arrows linking the menu to the device actions -->
      <g fill="none" stroke="var(--pink)" stroke-width="7" stroke-linecap="round">
        <path d="M268 355 C 300 400, 260 450, 300 480"/>
        <path d="M268 560 C 300 600, 280 650, 320 690"/>
        <path d="M348 712 L 490 712"/>
      </g>
      <g fill="var(--pink)">
        <path d="M288 470 L 312 478 L 296 498 Z"/>
        <path d="M308 680 L 332 692 L 312 708 Z"/>
        <path d="M486 700 L 506 712 L 486 724 Z"/>
      </g>
    </svg>

    <div class="brand">BrambleKeep</div>

    <h1 class="headline" aria-label="Lost UR phone?">
      <span class="word-lost">LOST</span>
      <span class="word-ur">UR</span>
      <span class="word-phone">PHONE?</span>
    </h1>

    <nav class="nav">
      <a class="nav-item" href="#">
        <svg viewBox="0 0 232 80"><polygon points="20,58 4,80 40,70" fill="var(--mint-deep)"/><polygon points="0,8 232,0 220,62 20,70" fill="var(--mint)"/></svg>
        <span>HOME</span>
      </a>
      <a class="nav-item" href="#">
        <svg viewBox="0 0 232 80"><polygon points="20,58 4,80 40,70" fill="var(--mint-deep)"/><polygon points="0,8 232,0 220,62 20,70" fill="var(--mint)"/></svg>
        <span>SERVICES</span>
      </a>
      <a class="nav-item" href="#">
        <svg viewBox="0 0 232 80"><polygon points="20,58 4,80 40,70" fill="var(--mint-deep)"/><polygon points="0,8 232,0 220,62 20,70" fill="var(--mint)"/></svg>
        <span>CONTACT US</span>
      </a>
    </nav>

    <div class="device device-lock" role="img" aria-label="Illustration of a mint tablet showing a padlock on its screen"></div>
    <div class="device device-apps" role="img" aria-label="Illustration of a pink tablet showing a grid of app icons"></div>

    <p class="actions">LOCK IT!<br>RING IT!<br>WIPE IT!</p>
    <p class="find">FIND IT!</p>
    <a class="cta" href="#">GET THE APP</a>
  </main>
</body>
</html>
```